Clearwave Motion Florida Billboard

We need a billboard designed for our physical therapy practice. Our billboard also serves as the sign for our building. We would like to have some sort of graphic notifying people driving by that our building is located here. Please go to www.clearwavemotionfl.example in order to get a better idea of our company.

Target Market(s)

Senior citizens having physical therapy

Industry/Entity Type

Healthcare- Physical Therapy

Colors
0094D4
00A9DD
6FCCEA
C7EBF8
E9F6FB

Requirements
Must have
• Must contain in bold the words "physical therapy". Must be highly visible from the road and have our company colors incorporated. Would also like to use the phrase "Relieving Pain. Restoring Function. Improving Lives."

```html
<!DOCTYPE html>
<html lang="en">
<head>
<meta charset="UTF-8">
<title>Clearwave Motion Florida – Physical Therapy Billboard</title>
<link rel="stylesheet" href="https://fonts.googleapis.com/css2?family=Montserrat:wght@500&family=Open+Sans:wght@400&family=Roboto:wght@700;900&display=swap">
<style>
  :root {
    --page-bg: #d9d9dc;
    --board-white: #ffffff;
    --ink: #111111;
    --brand-gray: #3a3a3c;
    --rule-gray: #bdbdbd;
    --sky-blue: #1fb5e6;
    --deep-blue: #0094d4;
    --lime: #8dc63f;
    --night: #0d0c26;
    --pale-blue: #c7ebf8;
  }
  html, body {
    margin: 0;
    width: 1200px;
    height: 1200px;
    overflow: hidden;
    background: var(--page-bg);
  }
  .billboard {
    position: absolute;
    left: 40px;
    top: 376px;
    width: 1120px;
    height: 448px;
    box-shadow: 0 18px 40px rgba(0,0,0,0.35);
  }
  .billboard svg { display: block; width: 100%; height: 100%; }
  .brand-name { font-family: "Montserrat", sans-serif; font-weight: 500; fill: var(--brand-gray); letter-spacing: 4px; }
  .headline { font-family: "Roboto", sans-serif; font-weight: 900; }
  .headline-blue { fill: var(--sky-blue); }
  .headline-green { fill: var(--lime); }
  .tagline { font-family: "Roboto", sans-serif; font-weight: 700; font-size: 38px; fill: var(--ink); }
  .web-address { font-family: "Open Sans", sans-serif; font-weight: 400; font-size: 36px; fill: #ffffff; }
  .phone-number { font-family: "Roboto", sans-serif; font-weight: 700; font-size: 66px; fill: var(--ink); }
</style>
</head>
<body>
<div class="billboard">
  <svg viewBox="0 0 1745 698" xmlns="http://www.w3.org/2000/svg">
    <defs>
      <linearGradient id="bandFade" x1="0" y1="0" x2="1" y2="0">
        <stop offset="0" stop-color="#ffffff"/>
        <stop offset="0.55" stop-color="#f1f1f1"/>
      </linearGradient>
      <linearGradient id="blueSweep" x1="0" y1="0" x2="0" y2="1">
        <stop offset="0" stop-color="var(--sky-blue)"/>
        <stop offset="1" stop-color="var(--deep-blue)"/>
      </linearGradient>
      <linearGradient id="photoTone" x1="0" y1="0" x2="0" y2="1">
        <stop offset="0" stop-color="#eeeeee"/>
        <stop offset="0.5" stop-color="#c9cbcf"/>
        <stop offset="1" stop-color="#9fa4ab"/>
      </linearGradient>
      <radialGradient id="spineGlow" cx="0.5" cy="0.5" r="0.5">
        <stop offset="0" stop-color="#3aa6c4" stop-opacity="0.75"/>
        <stop offset="0.6" stop-color="#1c5b78" stop-opacity="0.35"/>
        <stop offset="1" stop-color="var(--night)" stop-opacity="0"/>
      </radialGradient>
    </defs>

    <!-- base -->
    <rect class="board-base" width="1745" height="698" fill="url(#bandFade)"/>

    <!-- blue sweep and dark panel -->
    <path class="blue-sweep" d="M955,0 Q1340,340 955,698 H1115 Q1400,340 1040,0 Z" fill="url(#blueSweep)"/>
    <path class="dark-panel" d="M1040,0 H1745 V698 H1115 Q1400,340 1040,0 Z" fill="var(--night)"/>

    <!-- brand -->
    <circle class="brand-dot" cx="121" cy="113" r="72" fill="var(--sky-blue)"/>
    <rect class="brand-divider" x="210" y="36" width="4" height="152" fill="var(--brand-gray)"/>
    <text class="brand-name" x="238" y="84" font-size="40">CLEARWAVE</text>
    <text class="brand-name" x="238" y="133" font-size="40">MOTION</text>
    <text class="brand-name" x="238" y="170" font-size="24" letter-spacing="3">FLORIDA</text>

    <!-- location arrow -->
    <g class="location-marker">
      <polygon points="52,365 112,324 112,406" fill="var(--ink)"/>
      <circle cx="126" cy="362" r="28" fill="var(--ink)"/>
      <path d="M126,345 a12,12 0 0 1 12,12 c0,10 -12,22 -12,22 c0,0 -12,-12 -12,-22 a12,12 0 0 1 12,-12 z" fill="#ffffff"/>
      <circle cx="126" cy="357" r="5" fill="var(--ink)"/>
    </g>

    <!-- headline -->
    <text class="headline headline-blue" x="206" y="355" font-size="116" textLength="556" lengthAdjust="spacingAndGlyphs">PHYSICAL</text>
    <text class="headline headline-green" x="206" y="458" font-size="116" textLength="556" lengthAdjust="spacingAndGlyphs">THERAPY</text>

    <!-- taglines -->
    <rect class="tagline-rule" x="0" y="533" width="768" height="4" fill="var(--rule-gray)"/>
    <rect class="tagline-divider" x="288" y="566" width="4" height="132" fill="var(--rule-gray)"/>
    <rect class="tagline-divider" x="539" y="566" width="4" height="132" fill="var(--rule-gray)"/>
    <text class="tagline" x="82" y="612">RELIEVING</text>
    <text class="tagline" x="82" y="652">PAIN</text>
    <text class="tagline" x="315" y="612">RESTORING</text>
    <text class="tagline" x="315" y="652">FUNCTION</text>
    <text class="tagline" x="566" y="612">IMPROVING</text>
    <text class="tagline" x="566" y="652">LIVES</text>

    <!-- treatment photo area -->
    <circle class="photo-ring" cx="1072" cy="335" r="242" fill="#ffffff"/>
    <circle class="photo-area" cx="1066" cy="335" r="226" fill="url(#photoTone)" role="img" aria-label="Photo: therapist's gloved hands treating a patient's knee"/>

    <!-- spine illustration area -->
    <rect class="spine-area" x="1390" y="120" width="300" height="430" rx="40" fill="url(#spineGlow)" role="img" aria-label="Illustration: glowing blue human spine with light rings"/>

    <!-- web address -->
    <g class="globe-icon" fill="none" stroke="#ffffff" stroke-width="3">
      <circle cx="1150" cy="54" r="17"/>
      <ellipse cx="1150" cy="54" rx="7" ry="17"/>
      <line x1="1133" y1="54" x2="1167" y2="54"/>
      <line x1="1136" y1="44" x2="1164" y2="44"/>
      <line x1="1136" y1="64" x2="1164" y2="64"/>
    </g>
    <text class="web-address" x="1192" y="67" textLength="520" lengthAdjust="spacingAndGlyphs">www.clearwavemotionfl.example</text>

    <!-- phone band -->
    <polygon class="phone-band" points="1118,698 1200,588 1745,588 1745,698" fill="var(--lime)"/>
    <path class="phone-icon" d="M1238,622 c6,-4 10,-3 13,2 l7,11 c2,4 1,8 -3,10 l-5,3 c3,8 9,15 17,19 l3,-5 c2,-4 6,-5 10,-3 l11,7 c5,3 6,7 2,13 c-4,6 -10,9 -17,8 c-22,-5 -38,-22 -43,-44 c-1,-8 1,-16 5,-21 z" fill="var(--ink)"/>
    <text class="phone-number" x="1308" y="670" textLength="405" lengthAdjust="spacingAndGlyphs">941.555.0137</text>
  </svg>
</div>
</body>
</html>
```